Flyer Template

I need a flyer template for door knocking on properties. Text Boxes need to be editable, with a header and text body. Footer to be my info. Project to be stylized to match my real estate signs and logo art from past projects

```html
<!DOCTYPE html>
<html lang="en">
<head>
<meta charset="utf-8">
<title>Door-Knocking Flyer – Marlowe Realty</title>
<link href="https://fonts.googleapis.com/css2?family=Cinzel:wght@700&family=Mulish:wght@400&family=Jost:wght@400;500;600&display=swap" rel="stylesheet">
<style>
  :root{
    --bg:#e9e6e3;
    --paper:#ffffff;
    --red:#ee1c25;
    --red-dark:#b5121b;
    --red-deep:#a30d14;
    --ink:#2b2b2b;
    --grey:#4a4a4a;
    --black:#000000;
  }
  *{box-sizing:border-box;margin:0;padding:0}
  html,body{width:1200px;height:1200px;overflow:hidden;background:var(--bg)}
  .flyer{position:absolute;left:179px;top:5px;width:842px;height:1190px;background:var(--paper);overflow:hidden;box-shadow:0 4px 18px rgba(0,0,0,.18)}
  .hero{position:absolute;left:0;top:0}
  .brand-name{font-family:'Cinzel',serif;font-weight:700;fill:var(--ink);font-size:20px;letter-spacing:1px}
  .headline{position:absolute;left:0;width:842px;top:318px;text-align:center;font-family:'Cinzel',serif;font-weight:700;color:var(--red-dark);font-size:42px;line-height:42px}
  .subhead{position:absolute;left:0;width:842px;top:404px;text-align:center;font-family:'Cinzel',serif;font-weight:700;color:var(--grey);font-size:20px;line-height:30px}
  .intro{position:absolute;left:80px;width:682px;top:478px;text-align:center;font-family:'Mulish',sans-serif;color:var(--grey);font-size:18.5px;line-height:31px}
  .notice{position:absolute;left:0;top:585px;width:842px;height:75px;background:var(--red-dark);color:#fff;font-family:'Cinzel',serif;font-weight:700;font-size:20px;line-height:30px;text-align:center;padding-top:8px;letter-spacing:.5px}
  .photo{position:absolute}
  .section-title{position:absolute;font-family:'Cinzel',serif;font-weight:700;color:var(--red);font-size:19.5px;padding-bottom:3px;border-bottom:1.5px solid var(--grey);white-space:nowrap}
  .bullets{position:absolute;list-style:none;font-family:'Mulish',sans-serif;color:var(--grey);font-size:15.5px}
  .bullets li{height:32px;line-height:20px;padding-left:21px;position:relative;white-space:nowrap}
  .bullets li::before{content:"";position:absolute;left:0;top:6px;width:8px;height:8px;background:var(--red)}
  .contact{position:absolute;left:12px;top:1017px;width:818px;height:91px;background:var(--red);color:#fff;font-family:'Jost',sans-serif;text-align:center}
  .agent{position:absolute;left:0;width:818px;top:12px;font-weight:600;font-size:27px;letter-spacing:.5px;display:flex;justify-content:center;align-items:center;gap:20px}
  .agent::before,.agent::after{content:"";width:80px;height:1.5px;background:#fff}
  .details{position:absolute;left:0;width:818px;top:55px;font-size:19px;display:flex;justify-content:center;gap:26px}
  .details span{display:flex;align-items:center;gap:9px}
  .office{position:absolute;left:12px;top:1108px;width:818px;height:70px;background:var(--black);display:flex;align-items:center;justify-content:center}
  .office-name{font-family:'Jost',sans-serif;font-weight:500;color:#fff;font-size:23px;letter-spacing:1px}
</style>
</head>
<body>
<main class="flyer">
  <svg class="hero" width="842" height="470" viewBox="0 0 842 470">
    <defs>
      <linearGradient id="houseTone" x1="0" y1="0" x2="0" y2="1">
        <stop offset="0" stop-color="#8f95b8"/><stop offset=".55" stop-color="#6d7488"/><stop offset="1" stop-color="#4a4d57"/>
      </linearGradient>
      <linearGradient id="modelTone" x1="0" y1="0" x2="1" y2="1">
        <stop offset="0" stop-color="#c98a5a"/><stop offset=".5" stop-color="#d9a47a"/><stop offset="1" stop-color="#b8734a"/>
      </linearGradient>
    </defs>
    <rect x="0" y="0" width="422" height="440" fill="url(#houseTone)" role="img" aria-label="Photo of a two-storey family home at dusk"/>
    <rect x="422" y="0" width="420" height="470" fill="url(#modelTone)" role="img" aria-label="Photo of a hand holding a small model house"/>
    <path d="M300,0 L540,0 L520,150 Q510,188 470,188 L370,188 Q330,188 322,150 Z" fill="var(--paper)"/>
    <text class="brand-name" x="421" y="128" text-anchor="middle">MARLOWE</text>
    <text class="brand-name" x="421" y="152" text-anchor="middle">REALTY</text>
    <path d="M0,370 Q421,110 842,390 L842,470 L0,470 Z" fill="var(--red)"/>
    <path d="M0,392 Q421,130 842,418 L842,470 L0,470 Z" fill="var(--red-dark)"/>
    <path d="M0,430 Q421,140 842,450 L842,470 L0,470 Z" fill="var(--paper)"/>
  </svg>

  <h1 class="headline">Lorem ipsum<br>dolor</h1>
  <p class="subhead">sit amet, consectetuer adip-<br>iscing elit</p>
  <p class="intro">Lorem ipsum dolor sit amet, consectetuer adipiscing elit, sed diam nonummy nibh euismod tincidunt ut laoreet dolore magna aliquam erat volutpat. Ut wisi enim ad minim veniam,</p>

  <div class="notice">EACH OFFICE INDEPENDENTLY<br>OWNED AND OPERATED</div>

  <svg class="photo" style="left:68px;top:682px" width="250" height="151" role="img" aria-label="Photo of a person with a briefcase walking toward a front door">
    <rect width="250" height="151" fill="#8a8f84"/>
  </svg>
  <h2 class="section-title" style="left:345px;top:690px">Lorem ipsum dolor sit amet,</h2>
  <ul class="bullets" style="left:346px;top:738px">
    <li>Lorem ipsum dolor sit amet, consectetuer adipiscing elit,</li>
    <li>Lorem ipsum dolor sit amet, consectetuer adipiscing elit,</li>
    <li>Lorem ipsum dolor sit amet, consectetuer adipiscing elit,</li>
  </ul>

  <h2 class="section-title" style="left:73px;top:862px">Lorem ipsum dolor sit amet,</h2>
  <ul class="bullets" style="left:74px;top:910px">
    <li>Lorem ipsum dolor sit amet, consectetuer adipiscing elit,</li>
    <li>Lorem ipsum dolor sit amet, consectetuer adipiscing elit,</li>
    <li>Lorem ipsum dolor sit amet, consectetuer adipiscing elit,</li>
  </ul>
  <svg class="photo" style="left:559px;top:865px" width="231" height="130" role="img" aria-label="Photo of a person with a briefcase walking toward a front door">
    <rect width="231" height="130" fill="#8a8f84"/>
  </svg>

  <footer>
    <div class="contact">
      <div class="agent">JORDAN MARLOWE</div>
      <div class="details">
        <span><svg width="20" height="20" viewBox="0 0 24 24"><path fill="#fff" d="M6.6 10.8a15.1 15.1 0 0 0 6.6 6.6l2.2-2.2c.3-.3.7-.4 1-.2 1.1.4 2.3.6 3.6.6.6 0 1 .4 1 1V20c0 .6-.4 1-1 1A17 17 0 0 1 3 4c0-.6.4-1 1-1h3.5c.6 0 1 .4 1 1 0 1.3.2 2.5.6 3.6.1.3 0 .7-.2 1z"/></svg>555-014-2736</span>
        <span><svg width="22" height="16" viewBox="0 0 22 16"><rect width="22" height="16" fill="#fff"/><path d="M0,0 L11,9 L22,0" fill="none" stroke="var(--red)" stroke-width="2"/></svg>jmarlowe@example.com</span>
      </div>
    </div>
    <div class="office"><span class="office-name">NORTHFIELD GROUP</span></div>
  </footer>
</main>
</body>
</html>
```